Brochure for Flooring

Brochure for bamboo flooring company.

Size can be any size, we aren't married to specific dimension / type.

Files for logo, text, and some photos to get started attached. Designer can also use placeholder photos that we can switch out later.

Themes are Eco Friendly, natural, bamboo...

Thanks, and look forward to seeing your design.

Industry/Entity Type

Flooring

```html
<!DOCTYPE html>
<html lang="en">
<head>
<meta charset="utf-8">
<title>Sattva Bamboo Flooring Brochure</title>
<link rel="stylesheet" href="https://fonts.googleapis.com/css2?family=Patrick+Hand+SC&family=Arimo&display=swap">
<style>
  :root {
    --paper: #ffffff;
    --ink: #111111;
    --fold: #b5b5b5;
    --wood: #c28a45;
    --wood-dark: #6e4a26;
    --room: #7a4e2e;
    --leaf: #7fa23a;
    --cane: #8a9a86;
  }
  * { margin: 0; padding: 0; box-sizing: border-box; }
  html, body { width: 1200px; height: 969px; overflow: hidden; background: var(--paper); }
  .brochure {
    position: relative; width: 1200px; height: 969px; background: var(--paper);
    color: var(--ink); font-family: "Patrick Hand SC", "Comic Sans MS", cursive;
  }
  .fold-line {
    position: absolute; left: 584px; top: 0; height: 969px;
    border-left: 1px dashed var(--fold);
  }
  .photo { position: absolute; }
  .kitchen-photo {
    left: 0; top: 38px; width: 300px; height: 202px;
    background: linear-gradient(160deg, #5b5046 0%, #8c6a44 35%, var(--wood) 60%, #e0ae6a 100%);
  }
  .kitchen-title {
    position: absolute; left: 118px; top: 148px; color: #fff;
    font-size: 20px; letter-spacing: 1px;
  }
  .living-photo {
    left: 635px; top: 38px; width: 235px; height: 158px;
    background: linear-gradient(135deg, #d8c7a8 0%, #a9805a 45%, var(--room) 75%, #3e2a1c 100%);
  }
  .plant-photo {
    left: 15px; top: 665px; width: 160px; height: 145px;
    background: radial-gradient(ellipse at 40% 50%, var(--leaf) 0%, #b9cf86 45%, #ffffff 75%);
  }
  .cane-photo {
    left: 665px; top: 225px; width: 62px; height: 442px;
    background: linear-gradient(90deg, #ffffff 0%, var(--cane) 25%, #6f8a70 55%, #b9c2b6 85%, #ffffff 100%);
    -webkit-mask-image: linear-gradient(180deg, transparent 0%, #000 8%, #000 92%, transparent 100%);
    mask-image: linear-gradient(180deg, transparent 0%, #000 8%, #000 92%, transparent 100%);
  }
  .copy { position: absolute; font-size: 15px; letter-spacing: 0.6px; }
  .copy h2 { font-weight: normal; font-size: 18px; letter-spacing: 1px; line-height: 22px; }
  .eco-copy { left: 20px; top: 284px; width: 360px; line-height: 26.6px; }
  .fact-copy {
    position: absolute; left: 205px; top: 597px; width: 230px; height: 346px; overflow: hidden;
    font-family: "Arimo", Arial, sans-serif; font-size: 17px; line-height: 21.7px;
  }
  .coating-copy { left: 900px; top: 50px; width: 300px; line-height: 23.2px; }
  .lockfit-copy { left: 767px; top: 277px; width: 360px; line-height: 23.3px; }
  .lockfit-copy h2 { font-family: "Arimo", Arial, sans-serif; font-weight: bold; font-size: 19px; letter-spacing: 0.5px; }
  .lockfit-copy strong { font-family: "Arimo", Arial, sans-serif; font-size: 16px; }
  .install-copy { left: 767px; top: 416px; width: 380px; line-height: 23.3px; }
  .install-copy h2, .care-copy h2 { font-size: 15px; }
  .care-copy { left: 640px; top: 737px; width: 520px; line-height: 27px; }
</style>
</head>
<body>
<main class="brochure">
  <div class="fold-line"></div>

  <section class="page page-left">
    <div class="photo kitchen-photo" role="img" aria-label="Kitchen with a warm honey bamboo floor"></div>
    <div class="kitchen-title">Eco-Friendly</div>

    <p class="copy eco-copy">All Sattva Bamboo floors are built<br>with the environment in mind.<br>Renewable bamboo from well<br>managed plantations is sourced, with<br>the ecosystem in mind. Manufacturing<br>is done to keep pollutants to a<br>minimum. Emissions on finished<br>product exceed E-1 standards for<br>health and safety, and manufacturing<br>conditions are controlled to limit the<br>carbon footprint.</p>

    <div class="photo plant-photo" role="img" aria-label="Green bamboo stalk with leaves"></div>
    <p class="fact-copy">Bamboo is extremely environmentally friendly. Bamboo is a grass, not a wood, so it is a very renewable resource. Poles take 1 year to grow to full size, and 3 - 4 years to achieve maturity. Bamboo stand releases 35%more oxygen than any other tree. Bamboo helps conserve soil and the dense litter of bamboo leaves provide ideal material for compost manure.</p>
  </section>

  <section class="page page-right">
    <div class="photo living-photo" role="img" aria-label="Living room with leather sofas on a bamboo floor"></div>
    <div class="copy coating-copy">
      <h2>Coating</h2>
      <p>To ensure a lifetime of<br>beauty we use a registered<br>8-layer aluminum-oxide<br>German Technology, using<br>Halvor Coating.<br>Scratch and Wear Resistant,<br>it provides beautiful protection<br>to your bamboo floor.</p>
    </div>

    <div class="photo cane-photo" role="img" aria-label="Close view of a bamboo cane"></div>
    <div class="copy lockfit-copy">
      <h2>LOCKFIT</h2>
      <p>Interior floors are molded with the<br>patented <strong>LOCKFIT</strong> profile, which<br>allows for a fast, strong and glue-<br>free installation.</p>
    </div>

    <div class="copy install-copy">
      <h2>Installation</h2>
      <p>Contact a professional installer with<br>experience in solid wood flooring.<br>Floor must be installed over a dry,<br>flat substrate. Ensure that a moisture<br>barrier is put between sub-floor and<br>floor to prevent moisture creeping up.<br>To allow for expansion, make sure<br>there is a gap of 10mm between walls<br>and floor. For complete installation<br>instructions, please contact Greenline<br>Agro Works Private Limited or your<br>Local Distributor.</p>
    </div>

    <div class="copy care-copy">
      <h2>Maintenance</h2>
      <p>Proper maintenance your Sattva Bamboo Floor is<br>essential. Vacuum or sweep regularly. Use a damp mop;<br>avoid pools of water resting on the floor. Use floor<br>mats in all entry and exit ways. Cover sharp ends of<br>tables, chairs and appliances with felt shoes.</p>
    </div>
  </section>
</main>
</body>
</html>
```